New car stickers design and new office singage

we have recently rebranded and need a couple changes made, we aren't creative people so we want somebody to be creative for us and design our next new look. I have attached our branding guide and measurements required. Looking for a modern and professional look.

```html
<!DOCTYPE html>
<html lang="en">
<head>
<meta charset="utf-8">
<title>norvix — vehicle and office signage</title>
<link rel="stylesheet" href="https://fonts.googleapis.com/css2?family=Poppins:wght@400;500;600&family=Rajdhani:wght@500&display=swap">
<style>
  :root {
    --stage: #252525;
    --navy: #4161a3;
    --ring: #3a6db0;
    --sky: #22a7e0;
    --paper: #ffffff;
    --title: #ffffff;
  }
  html, body {
    margin: 0;
    padding: 0;
    width: 1200px;
    height: 796px;
    overflow: hidden;
    background: var(--stage);
  }
  .board { display: block; width: 1200px; height: 796px; }
  .section-title { font-family: "Rajdhani", sans-serif; font-weight: 500; fill: var(--title); text-anchor: middle; }
  .brand-name { font-family: "Poppins", sans-serif; font-weight: 600; fill: var(--navy); }
  .brand-name.on-dark { fill: var(--paper); }
  .brand-dot { fill: var(--navy); }
  .brand-dot.on-dark { fill: var(--paper); }
  .tagline { font-family: "Poppins", sans-serif; font-weight: 500; fill: var(--sky); }
  .tagline.on-dark { fill: var(--paper); }
  .value-label { font-family: "Poppins", sans-serif; font-weight: 600; font-size: 19px; fill: var(--paper); text-anchor: middle; }
  .contact { font-family: "Poppins", sans-serif; font-weight: 500; fill: var(--paper); }
  .contact.on-light { fill: var(--navy); }
  .phone-number { font-family: "Poppins", sans-serif; font-weight: 600; fill: var(--navy); }
  .phone-number.on-dark { fill: var(--paper); }
  .fill-navy { fill: var(--navy); }
  .fill-ring { fill: var(--ring); }
  .fill-sky { fill: var(--sky); }
  .fill-paper { fill: var(--paper); }
</style>
</head>
<body>
<svg class="board" viewBox="0 0 2364 1568" xmlns="http://www.w3.org/2000/svg">
  <defs>
    <clipPath id="window-clip"><rect x="201" y="153" width="911" height="391"/></clipPath>
    <clipPath id="window-inner"><circle cx="1090" cy="355" r="270"/></clipPath>
    <clipPath id="door-clip"><rect x="396" y="792" width="522" height="610"/></clipPath>
    <clipPath id="sign2-clip"><rect x="1476" y="1298" width="555" height="104"/></clipPath>
    <linearGradient id="ring-fade" x1="0" y1="0" x2="1" y2="1">
      <stop offset="0" stop-color="#4161a3"/>
      <stop offset="1" stop-color="#2a8ad0"/>
    </linearGradient>
    <symbol id="icon-phone" viewBox="0 0 24 24">
      <path d="M6.6 10.8a15.1 15.1 0 0 0 6.6 6.6l2.2-2.2a1 1 0 0 1 1-.25 11.4 11.4 0 0 0 3.6.57 1 1 0 0 1 1 1V20a1 1 0 0 1-1 1A17 17 0 0 1 3 4a1 1 0 0 1 1-1h3.5a1 1 0 0 1 1 1c0 1.25.2 2.45.57 3.570a1 1 0 0 1-.25 1z"/>
    </symbol>
    <symbol id="icon-mail" viewBox="0 0 24 18">
      <rect x="1" y="1" width="22" height="16" fill="none" stroke="currentColor" stroke-width="2"/>
      <path d="M1 1l11 9 11-9M1 17l8-7M23 17l-8-7" fill="none" stroke="currentColor" stroke-width="2"/>
    </symbol>
  </defs>

  <!-- Section titles -->
  <text class="section-title" x="656" y="116" font-size="44">Windows Print</text>
  <text class="section-title" x="1735" y="116" font-size="44">Car Door</text>
  <text class="section-title" x="656" y="750" font-size="58">Door Print</text>
  <text class="section-title" x="1735" y="592" font-size="44">Car Glass</text>
  <text class="section-title" x="1735" y="977" font-size="44">Sign  1</text>
  <text class="section-title" x="1735" y="1258" font-size="44">Sign 2</text>

  <!-- Windows print -->
  <g class="window-print" clip-path="url(#window-clip)">
    <rect class="fill-navy" x="201" y="153" width="911" height="391"/>
    <path class="fill-sky" d="M201 153 H228 L262 187 H201 Z"/>
    <rect class="fill-paper" x="201" y="187" width="560" height="174"/>
    <path class="fill-sky" d="M296 361 H356 Q340 470 310 544 H230 Q290 470 296 361 Z"/>
    <circle class="fill-paper" cx="1090" cy="355" r="386"/>
    <circle class="fill-ring" cx="1090" cy="355" r="332"/>
    <circle class="fill-paper" cx="1090" cy="355" r="268"/>
    <g clip-path="url(#window-inner)">
      <rect class="fill-sky" x="800" y="197" width="300" height="52"/>
      <rect class="fill-sky" x="800" y="263" width="300" height="51"/>
      <rect class="fill-sky" x="800" y="327" width="300" height="51"/>
      <rect class="fill-sky" x="800" y="393" width="300" height="50"/>
      <rect class="fill-sky" x="800" y="457" width="300" height="50"/>
    </g>
    <rect class="fill-sky" x="1100" y="153" width="12" height="391"/>
    <text class="value-label" x="966" y="232">RELATIONSHIP</text>
    <text class="value-label" x="957" y="297">STAYING COMPETITIVE</text>
    <text class="value-label" x="966" y="360">INNOVATIVE TECHNOLOGY</text>
    <text class="value-label" x="916" y="426">EXPERTISE</text>
    <text class="value-label" x="963" y="488">PEACE OF MIND</text>

    <circle class="brand-dot" cx="296" cy="278" r="62"/>
    <text class="brand-name" x="386" y="300" font-size="100">norvix</text>
    <text class="tagline" x="390" y="326" font-size="15" textLength="300" lengthAdjust="spacing">SUPPORT · NETWORK · SECURE</text>

    <use href="#icon-mail" x="313" y="430" width="24" height="18" color="#ffffff"/>
    <text class="contact" x="362" y="446" font-size="22">hello@norvix.com.au</text>
    <g fill="none" stroke="#ffffff" stroke-width="2.2">
      <circle cx="314" cy="479" r="12"/>
      <ellipse cx="314" cy="479" rx="5" ry="12"/>
      <path d="M302 479 H326 M304 473 H324 M304 485 H324"/>
    </g>
    <text class="contact" x="352" y="487" font-size="22">www.norvix.com.au</text>
    <path fill="#ffffff" d="M300 505 a11 11 0 0 1 11 11 c0 8-11 19-11 19 s-11-11-11-19 a11 11 0 0 1 11-11 z M300 512 a4 4 0 1 0 0.01 0z" fill-rule="evenodd"/>
    <text class="contact" x="345" y="521" font-size="16">14 Alder Lane, Yarra Glen, Victoria, 3775</text>
  </g>

  <!-- Car door -->
  <g class="car-door">
    <rect class="fill-paper" x="1528" y="153" width="452" height="335"/>
    <circle class="brand-dot" cx="1602" cy="255" r="52"/>
    <text class="brand-name" x="1674" y="277" font-size="88">norvix</text>
    <text class="tagline" x="1678" y="297" font-size="13" textLength="264" lengthAdjust="spacing">SUPPORT · NETWORK · SECURE</text>
    <circle class="fill-navy" cx="1590" cy="367" r="25"/>
    <use href="#icon-phone" x="1578" y="355" width="24" height="24" fill="#ffffff"/>
    <text class="phone-number" x="1626" y="385" font-size="50">1300 555 019</text>
    <text class="contact on-light" x="1762" y="440" font-size="28" text-anchor="middle">www.norvix.com.au</text>
  </g>

  <!-- Car glass -->
  <g class="car-glass">
    <rect class="fill-paper" x="1384" y="614" width="740" height="250"/>
    <circle class="brand-dot" cx="1540" cy="710" r="72"/>
    <text class="brand-name" x="1640" y="735" font-size="115">norvix</text>
    <text class="tagline" x="1645" y="764" font-size="17" textLength="345" lengthAdjust="spacing">SUPPORT · NETWORK · SECURE</text>
    <circle class="fill-navy" cx="1594" cy="818" r="28"/>
    <use href="#icon-phone" x="1580" y="804" width="28" height="28" fill="#ffffff"/>
    <text class="phone-number" x="1635" y="838" font-size="55">1300 555 019</text>
  </g>

  <!-- Sign 1 -->
  <g class="sign-one">
    <rect class="fill-navy" x="1175" y="1002" width="1122" height="142"/>
    <rect class="fill-paper" x="1215" y="1002" width="530" height="142"/>
    <circle class="brand-dot" cx="1313" cy="1071" r="50"/>
    <text class="brand-name" x="1390" y="1090" font-size="85">norvix</text>
    <text class="tagline" x="1393" y="1110" font-size="12" textLength="255" lengthAdjust="spacing">SUPPORT · NETWORK · SECURE</text>
    <circle class="fill-paper" cx="1823" cy="1046" r="32"/>
    <use href="#icon-phone" x="1807" y="1030" width="32" height="32" fill="#4161a3"/>
    <text class="phone-number on-dark" x="1866" y="1068" font-size="58">1300 555 019</text>
    <use href="#icon-mail" x="1866" y="1094" width="40" height="30" color="#ffffff"/>
    <text class="contact" x="1922" y="1119" font-size="32">hello@norvix.com.au</text>
  </g>

  <!-- Sign 2 -->
  <g class="sign-two" clip-path="url(#sign2-clip)">
    <rect class="fill-paper" x="1476" y="1298" width="555" height="104"/>
    <circle cx="1440" cy="1360" r="90" fill="none" stroke="#4161a3" stroke-width="16"/>
    <circle cx="2060" cy="1360" r="90" fill="none" stroke="#4161a3" stroke-width="16"/>
    <circle class="brand-dot" cx="1634" cy="1350" r="38"/>
    <text class="brand-name" x="1692" y="1366" font-size="66">norvix</text>
    <text class="tagline" x="1696" y="1382" font-size="10" textLength="198" lengthAdjust="spacing">SUPPORT · NETWORK · SECURE</text>
  </g>

  <!-- Door print -->
  <g class="door-print" clip-path="url(#door-clip)">
    <rect class="fill-paper" x="396" y="792" width="522" height="610"/>
    <rect class="fill-sky" x="396" y="820" width="400" height="38"/>
    <text class="contact" x="418" y="853" font-size="34">hello@norvix.com.au</text>
    <circle cx="918" cy="843" r="120" fill="none" stroke="url(#ring-fade)" stroke-width="29"/>
    <rect class="fill-navy" x="396" y="985" width="522" height="196"/>
    <circle class="brand-dot on-dark" cx="482" cy="1087" r="62"/>
    <text class="brand-name on-dark" x="572" y="1110" font-size="100">norvix</text>
    <text class="tagline on-dark" x="576" y="1136" font-size="15" textLength="300" lengthAdjust="spacing">SUPPORT · NETWORK · SECURE</text>
    <rect class="fill-navy" x="500" y="1323" width="418" height="39"/>
    <circle cx="396" cy="1330" r="97" fill="none" stroke="#22a7e0" stroke-width="29"/>
    <text class="contact" x="714" y="1355" font-size="34" text-anchor="middle">www.norvix.com.au</text>
  </g>
</svg>
</body>
</html>
```